Dorsey K. Wendell Business Card

We need a business card for our company Dorsey K. Wendell Heating & Plumbing to be distributed to potential customers. It should follow the color scheme of our logo and have a modern upscale and masculine look.

The logo is attached and the info below should also be included:

5187 W. Cedar Brook Rd.
Larkfield, PA 17588

Russell T. Wendell
(717) 592-0817
russelltwendell@fernmail.net
dorseykwendell.net
PA #093148

Industry/Entity Type

Business

Contact Information for Business Card

5187 W. Cedar Brook Rd.
Larkfield, PA 17588

Russell T. Wendell
(717) 592-0817
russelltwendell@fernmail.net
dorseykwendell.net
PA #093148

Colors

Designer to choose colors to be used in the design.

Requirements
Must have
• Information above included

```html
<!DOCTYPE html>
<html lang="en">
<head>
<meta charset="utf-8">
<title>Dorsey K. Wendell Business Card</title>
<link rel="stylesheet" href="https://fonts.googleapis.com/css2?family=Oswald:wght@300;400;500;600&family=Poppins:wght@400&display=swap">
<style>
  :root {
    --brand-blue: #0b57a8;
    --brand-green: #a6d13a;
    --ink: #2b2b2b;
    --rule: #b9b9b9;
    --card: #ffffff;
    --backdrop: #e8e5e1;
  }
  * { margin: 0; padding: 0; box-sizing: border-box; }
  html, body { width: 1200px; height: 1200px; overflow: hidden; background: var(--backdrop); }
  .canvas { position: relative; width: 1200px; height: 1200px; }
  .card {
    position: absolute; left: 148px; width: 904px; height: 518px;
    background: var(--card); border-radius: 38px; overflow: hidden;
    box-shadow: 0 6px 18px rgba(0,0,0,0.18);
    font-family: "Oswald", sans-serif; color: var(--ink);
  }
  .card--front { top: 52px; }
  .card--back { top: 618px; }

  .brand { position: absolute; display: flex; align-items: center; }
  .brand__square { background: var(--brand-blue); flex: none; }
  .brand__name { color: var(--brand-blue); font-weight: 600; white-space: nowrap; letter-spacing: 0.5px; }

  .card--front .brand { right: 52px; top: 64px; gap: 16px; }
  .card--front .brand__square { width: 72px; height: 72px; }
  .card--front .brand__name { font-size: 42px; }

  .license { position: absolute; right: 50px; top: 160px; font-size: 22px; font-weight: 400; }

  .person { position: absolute; left: 52px; top: 284px; }
  .person__name { font-size: 40px; font-weight: 500; color: var(--brand-blue); line-height: 1.1; }
  .person__title { font-family: "Poppins", sans-serif; font-size: 20px; letter-spacing: 0.5px; margin-top: 0; }
  .divider { position: absolute; left: 282px; right: 0; top: 347px; height: 1.5px; background: var(--rule); }

  .contact { position: absolute; left: 62px; top: 380px; list-style: none; }
  .contact__item { display: flex; align-items: center; gap: 22px; height: 27px; font-size: 20px; font-weight: 300; }
  .contact__icon { width: 20px; height: 18px; fill: var(--brand-blue); flex: none; }

  .address { position: absolute; right: 51px; top: 380px; text-align: right; font-style: normal; font-size: 20px; font-weight: 300; line-height: 27px; }
  .address__company { color: var(--brand-blue); font-weight: 500; }

  .band { position: absolute; left: 0; bottom: 0; width: 904px; height: 22px; }

  .card--back .brand { left: 0; right: 0; top: 0; bottom: 0; justify-content: center; gap: 24px; }
  .card--back .brand__square { width: 110px; height: 110px; }
  .card--back .brand__name { font-size: 64px; }
</style>
</head>
<body>
<main class="canvas">
  <section class="card card--front" aria-label="Card front">
    <div class="brand">
      <span class="brand__square"></span>
      <span class="brand__name">DORSEY K. WENDELL</span>
    </div>
    <p class="license">PA #093148</p>

    <div class="person">
      <h1 class="person__name">RUSSELL T. WENDELL</h1>
      <p class="person__title">Managing Director</p>
    </div>
    <div class="divider"></div>

    <ul class="contact">
      <li class="contact__item">
        <svg class="contact__icon" viewBox="0 0 24 24" aria-hidden="true"><path d="M6.6 10.8a15.1 15.1 0 0 0 6.6 6.6l2.2-2.2c.3-.3.7-.4 1-.2 1.1.4 2.3.6 3.6.6.6 0 1 .4 1 1V20c0 .6-.4 1-1 1A17 17 0 0 1 3 4c0-.6.4-1 1-1h3.5c.6 0 1 .4 1 1 0 1.3.2 2.5.6 3.6.1.3 0 .7-.2 1z"/></svg>
        <span>(717) 592-0817</span>
      </li>
      <li class="contact__item">
        <svg class="contact__icon" viewBox="0 0 24 18" aria-hidden="true"><path d="M0 0h24v18H0z" fill="var(--brand-blue)"/><path d="M1.5 1.5 12 10 22.5 1.5 M1.5 16.5 9 9 M22.5 16.5 15 9" stroke="#fff" stroke-width="1.6" fill="none"/></svg>
        <span>russelltwendell@fernmail.net</span>
      </li>
      <li class="contact__item">
        <svg class="contact__icon" viewBox="0 0 24 24" aria-hidden="true"><circle cx="12" cy="12" r="11"/><path d="M12 1v22M1 12h22M12 1c-4 3-4 19 0 22M12 1c4 3 4 19 0 22" stroke="#fff" stroke-width="1.4" fill="none"/></svg>
        <span>www.dorseykwendell.net</span>
      </li>
    </ul>

    <address class="address">
      <div class="address__company">Dorsey K. Wendell - Heating &amp; Plumbing</div>
      <div>5187 W. Cedar Brook Rd.</div>
      <div>Larkfield, PA 17588</div>
    </address>

    <svg class="band" viewBox="0 0 904 22" preserveAspectRatio="none" aria-hidden="true">
      <polygon points="0,0 460,0 438,22 0,22" fill="var(--brand-green)"/>
      <polygon points="474,0 904,0 904,22 452,22" fill="var(--brand-blue)"/>
    </svg>
  </section>

  <section class="card card--back" aria-label="Card back">
    <div class="brand">
      <span class="brand__square"></span>
      <span class="brand__name">DORSEY K. WENDELL</span>
    </div>
  </section>
</main>
</body>
</html>
```